Business Card Design

Velvet Pixel Promotions

An online marketing consulting & strategy business for the cosmetic niche

We specialise in Increasing Leads, Conversions & Content Marketing

I am looking for a very clean, BOLD business card that is simple & effective

Target Market(s)

cosmetic surgeons & cosmetic clinics

Industry/Entity Type

Marketing

Contact Information for Business Card

Darren Okoye
Online Marketing Strategist

Darren@VelvetPixelPromotions.example
0491 268 517

Connectly: in/darrenokoye

```html
<!DOCTYPE html>
<html lang="en">
<head>
<meta charset="utf-8">
<title>Velvet Pixel Promotions – Business Card</title>
<link rel="stylesheet" href="https://fonts.googleapis.com/css2?family=Arimo:wght@400;700&display=swap">
<style>
  :root {
    --backdrop: #2b2b2b;
    --card-white: #ffffff;
    --green-pale: #b7d66a;
    --green-mid: #7bb23a;
    --green-deep: #4c9a2e;
    --green-brand: #5cb543;
    --green-back-top: #6cc04a;
    --green-back-bottom: #4a9f33;
    --text-grey: #9a9a9a;
    --text-dark: #1f1f1f;
    --network-blue: #2f9fd6;
  }
  html, body {
    margin: 0;
    padding: 0;
    width: 1200px;
    height: 1000px;
    overflow: hidden;
    background: var(--backdrop);
    font-family: "Arimo", Arial, sans-serif;
  }
  .card {
    position: absolute;
    left: 215px;
    width: 770px;
    height: 440px;
    overflow: hidden;
    box-shadow: 0 10px 30px rgba(0,0,0,0.45);
  }
  .card-back {
    top: 40px;
    background: linear-gradient(160deg, var(--green-back-top), var(--green-back-bottom));
    display: flex;
    align-items: center;
    justify-content: center;
  }
  .card-front {
    top: 520px;
    background: var(--card-white);
  }
  .accent-area {
    position: absolute;
    top: 0;
    right: 0;
    width: 300px;
    height: 100%;
    background: linear-gradient(160deg, var(--green-pale) 0%, var(--green-mid) 45%, var(--green-deep) 100%);
  }
  .brand {
    display: flex;
    align-items: center;
    gap: 14px;
  }
  .brand-dot {
    border-radius: 50%;
    flex: none;
  }
  .brand-name {
    font-weight: 400;
    text-transform: uppercase;
    letter-spacing: 0.12em;
    line-height: 1.05;
  }
  .card-back .brand-dot {
    width: 64px;
    height: 64px;
    background: var(--card-white);
  }
  .card-back .brand-name {
    color: var(--card-white);
    font-size: 30px;
  }
  .card-front .brand {
    position: absolute;
    left: 50px;
    top: 50px;
  }
  .card-front .brand-dot {
    width: 44px;
    height: 44px;
    background: var(--green-brand);
  }
  .card-front .brand-name {
    color: var(--text-dark);
    font-size: 19px;
  }
  .person {
    position: absolute;
    left: 50px;
    top: 180px;
  }
  .person-name {
    margin: 0;
    font-size: 40px;
    font-weight: 700;
    color: var(--green-brand);
    letter-spacing: -0.01em;
  }
  .person-role {
    margin: 2px 0 0;
    font-size: 18px;
    color: var(--text-grey);
  }
  .contacts {
    position: absolute;
    left: 50px;
    top: 292px;
    margin: 0;
    padding: 0;
    list-style: none;
    font-size: 19px;
    color: var(--text-dark);
  }
  .contacts li {
    display: flex;
    align-items: center;
    gap: 10px;
    height: 29px;
    white-space: nowrap;
  }
  .contact-icon {
    width: 18px;
    height: 18px;
    background: var(--green-brand);
    color: var(--card-white);
    font-size: 13px;
    font-weight: 700;
    display: flex;
    align-items: center;
    justify-content: center;
    border-radius: 2px;
  }
  .network-label {
    color: var(--network-blue);
    font-weight: 700;
  }
</style>
</head>
<body>

<section class="card card-back" aria-label="Business card back">
  <div class="brand">
    <span class="brand-dot"></span>
    <span class="brand-name">Velvet<br>Pixel<br>Promotions</span>
  </div>
</section>

<section class="card card-front" aria-label="Business card front">
  <div class="accent-area" role="img" aria-label="Decorative green accent area"></div>

  <div class="brand">
    <span class="brand-dot"></span>
    <span class="brand-name">Velvet<br>Pixel<br>Promotions</span>
  </div>

  <div class="person">
    <h1 class="person-name">Darren Okoye</h1>
    <p class="person-role">Online Marketing Strategist</p>
  </div>

  <ul class="contacts">
    <li><span class="contact-icon">p</span>0491 268 517</li>
    <li><span class="contact-icon">e</span>Darren@VelvetPixelPromotions.example</li>
    <li><span class="contact-icon">w</span>www.VelvetPixelPromotions.example</li>
    <li><span><span class="network-label">Connectly</span>: in/darrenokoye</span></li>
  </ul>
</section>

</body>
</html>
```